Dental Business Card

I need Dental oriented business cards.
On the front side -
- on the first line, my name:
Dr Marlo Vintner
- on the second line (just underneath):
Doctor of Dental Medicine
- on the third line, or underneath that or in a corner, I would like the address and phone number:
5182 Ch. Birchfield
Montreal QC H2T 4B9
514-629-5074
- other than that i would maybe like a logo of a tooth, but i want it to be subtle and very basic!
- I would like the card to be preferably black or dark grey-ish with the writing in white
On the other side -
- 2-3 lines with the possibility to write the next appointment the box with the lines should be white, with the rest of the card being black

```html
<!DOCTYPE html>
<html lang="en">
<head>
<meta charset="utf-8">
<title>Dental Business Card — Dr Marlo Vintner</title>
<link rel="stylesheet" href="https://fonts.googleapis.com/css2?family=Tinos:wght@400;700&display=swap">
<style>
  :root {
    --stage: #232323;
    --card: #131313;
    --ink: #ffffff;
    --ink-soft: #e6e6e6;
    --mark: #2a2a2a;
    --rule: #cfcfcf;
  }
  * { box-sizing: border-box; margin: 0; padding: 0; }
  html, body {
    width: 1200px; height: 900px; overflow: hidden;
    background: var(--stage);
    font-family: "Tinos", "Times New Roman", serif;
    color: var(--ink);
  }
  .stage {
    width: 1200px; height: 900px;
    display: flex; flex-direction: column; align-items: center; justify-content: center;
    gap: 44px;
  }
  .card {
    position: relative;
    width: 640px; height: 366px;
    background: var(--card);
    box-shadow: 0 10px 28px rgba(0,0,0,.55);
    overflow: hidden;
  }
  .card__mark {
    position: absolute;
    font-weight: 700;
    color: var(--mark);
    white-space: nowrap;
    line-height: 1;
  }
  /* Appointment side */
  .appointment .card__mark { font-size: 28px; right: 40px; bottom: 16px; }
  .appointment__title {
    position: absolute; left: 0; right: 0; top: 66px;
    text-align: center; padding-left: 90px;
    font-weight: 700; font-size: 26px; letter-spacing: .5px;
  }
  .appointment__fields {
    position: absolute; left: 70px; right: 70px; top: 150px;
    list-style: none;
  }
  .appointment__field {
    display: flex; align-items: flex-end;
    height: 54px;
    font-size: 17px; color: var(--ink-soft);
  }
  .appointment__label { width: 62px; }
  .appointment__line {
    flex: 1; margin-left: 14px; margin-bottom: 4px;
    border-bottom: 1px dashed var(--rule);
  }
  /* Front side */
  .front .card__mark { font-size: 44px; right: 40px; top: 150px; }
  .front__name {
    position: absolute; left: 66px; top: 48px;
    font-weight: 700; font-size: 36px; letter-spacing: .5px;
  }
  .front__title {
    position: absolute; left: 64px; top: 96px;
    font-size: 19px; color: var(--ink-soft);
  }
  .front__contact {
    position: absolute; left: 60px; bottom: 62px;
    list-style: none; font-size: 18px; color: var(--ink-soft);
  }
  .front__contact li { display: flex; line-height: 34px; }
  .front__key { width: 30px; font-size: 22px; }
</style>
</head>
<body>
<main class="stage">
  <section class="card appointment" aria-label="Appointment side">
    <span class="card__mark">Vintner Dental</span>
    <h2 class="appointment__title">APPOINTMENT</h2>
    <ul class="appointment__fields">
      <li class="appointment__field"><span class="appointment__label">For:</span><span class="appointment__line"></span></li>
      <li class="appointment__field"><span class="appointment__label">Date:</span><span class="appointment__line"></span></li>
      <li class="appointment__field"><span class="appointment__label">Time:</span><span class="appointment__line"></span></li>
    </ul>
  </section>

  <section class="card front" aria-label="Front side">
    <span class="card__mark">Vintner Dental</span>
    <h1 class="front__name">Dr Marlo Vintner</h1>
    <p class="front__title">Doctor of Dental Medicine</p>
    <ul class="front__contact">
      <li><span class="front__key">P</span>: 514-629-5074</li>
      <li><span class="front__key">A</span>: 5182 Ch. Birchfield Montreal QC H2T 4B9</li>
    </ul>
  </section>
</main>
</body>
</html>
```